Original business card of a small accounting firm

My firm specializes in accounting and taxes for small businesses. I'm looking for an original and creative business card as a marketing tool to give to prospective clients; however since we are a professional firm the card must also appear professional. I'm uploading a few examples of what I believe may fit my needs. Please feel free to use them as a jumping off point. Lastly, I'm uploading the company logo which I'd like to be the focal point on the back of the card and somewhat incorporated on the front on a smaller scale. I hope my description was helpful.
Target Market(s)
Tax clients and small businesses
Industry/Entity Type
Accounting
Contact Information for Business Card
Gerald Whitcombe
Certified Public Accountant │President
Whitcombe Advisors
T│ (555) 417-2863
Email│GWhitcombe@WhitcombeAdvisors.example
Look and feel
Each slider illustrates characteristics of the customer's brand and the style your logo design should communicate.

```html
<!DOCTYPE html>
<html lang="en">
<head>
<meta charset="utf-8">
<title>Whitcombe Advisors – Business Card</title>
<link rel="stylesheet" href="https://fonts.googleapis.com/css2?family=Lato:wght@400;700&family=Cinzel:wght@400&display=swap">
<style>
  :root {
    --backdrop: #dcdcdd;
    --card: #f7f7f6;
    --ink: #3a3a3c;
    --ink-soft: #555558;
    --brand-blue: #1f4fa8;
    --link-blue: #2a57b3;
    --tint-light: #c9d3ec;
    --tint-mid: #8fa3d6;
    --shadow: rgba(0, 0, 0, 0.16);
  }
  * { box-sizing: border-box; margin: 0; padding: 0; }
  html, body {
    width: 1200px; height: 1000px; overflow: hidden;
    background: var(--backdrop);
    font-family: "Lato", Arial, sans-serif;
    color: var(--ink);
  }
  .canvas { position: relative; width: 1200px; height: 1000px; }
  .card {
    position: absolute; width: 560px; height: 320px;
    background: var(--card);
    box-shadow: 0 14px 30px var(--shadow);
    overflow: hidden;
  }
  .card--back { left: 560px; top: 150px; }
  .card--front { left: 110px; top: 530px; }

  /* Back: brand focal point */
  .brand-lockup {
    position: absolute; inset: 0;
    display: flex; flex-direction: column; align-items: center; justify-content: center;
    gap: 14px;
  }
  .brand-name {
    display: flex; align-items: center; gap: 14px;
    font-weight: 700; font-size: 40px; color: var(--ink); letter-spacing: 0.5px;
  }
  .brand-mark { width: 30px; height: 30px; background: var(--brand-blue); }
  .brand-tagline {
    font-family: "Cinzel", Georgia, serif; font-size: 17px; letter-spacing: 2px;
    color: var(--ink-soft); text-transform: uppercase;
  }

  /* Front: contact side */
  .front-brand {
    position: absolute; left: 34px; top: 30px;
    display: flex; align-items: center; gap: 8px;
    font-weight: 700; font-size: 15px; color: var(--ink);
  }
  .front-brand .brand-mark { width: 12px; height: 12px; }
  .front-accent {
    position: absolute; left: 0; top: 130px; width: 210px; height: 150px;
    background: linear-gradient(120deg, var(--tint-mid) 0%, var(--tint-light) 70%, rgba(201,211,236,0) 100%);
    opacity: 0.75;
  }
  .contact {
    position: absolute; right: 36px; top: 112px; text-align: right;
  }
  .contact-name { font-weight: 700; font-size: 25px; color: var(--ink); }
  .contact-name .surname { color: var(--brand-blue); }
  .contact-role { font-size: 14px; line-height: 1.3; color: var(--ink-soft); margin-top: 2px; }
  .contact-lines { margin-top: 14px; text-align: left; display: inline-block; font-size: 14px; line-height: 1.7; }
  .contact-lines dt { display: inline-block; width: 22px; color: var(--ink-soft); }
  .contact-lines dd { display: inline; color: var(--link-blue); }
  .contact-lines div { white-space: nowrap; }
</style>
</head>
<body>
<main class="canvas">
  <section class="card card--back" aria-label="Card back">
    <div class="brand-lockup">
      <div class="brand-name"><span class="brand-mark"></span>Whitcombe Advisors</div>
      <div class="brand-tagline">Small Business Accounting and Taxes</div>
    </div>
  </section>

  <section class="card card--front" aria-label="Card front">
    <div class="front-brand"><span class="brand-mark"></span>Whitcombe Advisors</div>
    <div class="front-accent" role="img" aria-label="Soft blue brand accent"></div>
    <div class="contact">
      <div class="contact-name">Gerald <span class="surname">Whitcombe</span></div>
      <div class="contact-role">Certified Public Accountant<br>President Whitcombe Advisors</div>
      <dl class="contact-lines">
        <div><dt>E:</dt><dd>GWhitcombe@WhitcombeAdvisors.example</dd></div>
        <div><dt>T:</dt><dd>(555) 417-2863</dd></div>
      </dl>
    </div>
  </section>
</main>
</body>
</html>
```